New website for tarnova.se using wordpress

- Tarnova is a consultant broker based in Sweden
- Current web page: tarnova.se
- We want a new web page and we are aiming for simple and "clean"
- Two target groups:
1. Consultants/Consultant firms looking for assignments
2. Clients looking for consultants
- Colors + Logo attached

Requirements
Must have
• The new site should have separate pages the different sections. We have to be able to link to each page separately. NOT like the current web page where all the content is on one page.

```html
<!DOCTYPE html>
<html lang="sv">
<head>
<meta charset="utf-8">
<title>Tarnova – Konsultmäklare</title>
<link href="https://fonts.googleapis.com/css2?family=Montserrat:wght@400;500;600;700&display=swap" rel="stylesheet">
<style>
:root{
  --purple:#5a2d91;
  --purple-dark:#3f1d6b;
  --ink:#1d1d1f;
  --muted:#6e6e73;
  --line:#dcdce0;
  --grey:#f3f3f4;
  --white:#ffffff;
  --photo-a:#cfc8c2;
  --photo-b:#9c958f;
}
*{box-sizing:border-box;margin:0;padding:0}
html,body{width:1200px;height:4036px;overflow:hidden;background:var(--white)}
body{font-family:"Montserrat",Arial,sans-serif;color:var(--ink);font-size:13px;line-height:1.6}
.wrap{width:960px;margin:0 auto;position:relative}
h2{font-size:32px;font-weight:700;line-height:1.15;letter-spacing:.5px}
.section{position:relative}
.section.grey{background:var(--grey)}
.side-label{position:absolute;left:-40px;top:6px;writing-mode:vertical-rl;transform:rotate(180deg);font-size:9px;letter-spacing:3px;color:var(--purple);text-transform:uppercase}
.photo{background:linear-gradient(135deg,var(--photo-a),var(--photo-b))}

/* header */
.site-header{height:64px}
.site-header .wrap{display:flex;align-items:center;justify-content:space-between;height:64px}
.brand{display:flex;align-items:center;gap:8px;font-weight:700;font-size:20px;color:var(--purple)}
.brand-dot{width:12px;height:12px;background:var(--purple)}
.nav{display:flex;gap:28px;align-items:center;font-size:11px}
.nav .cta{background:var(--purple);color:var(--white);padding:7px 16px}

/* hero */
.hero{height:246px}
.hero .wrap{display:flex;justify-content:space-between;padding-top:28px}
.kicker{font-size:10px;letter-spacing:3px;color:var(--purple);text-transform:uppercase;margin-bottom:10px}
.hero h1{font-size:44px;line-height:1.12;font-weight:700;color:var(--purple);width:640px}
.hero-aside{width:160px;font-size:10px;color:var(--muted);padding-top:110px}
.hero-photo{height:320px}

/* söker du */
.seek{height:390px;padding-top:70px}
.seek .wrap{padding-left:80px}
.seek h2{width:340px;margin-bottom:20px}
.seek p{width:480px;color:var(--muted);font-size:11px;margin-bottom:18px}
.ticks{list-style:none;width:460px}
.ticks li{display:flex;gap:12px;font-size:11px;color:var(--muted);margin-bottom:10px}
.ticks svg{flex:none;margin-top:2px}

/* kompetens */
.areas{height:420px;padding-top:56px}
.areas .wrap{padding-left:80px}
.areas-badge{position:absolute;right:0;top:30px;background:var(--purple);color:var(--white);font-weight:700;font-size:12px;padding:8px 14px}
.areas h2{width:420px;margin-bottom:36px}
.area-grid{display:grid;grid-template-columns:repeat(6,1fr);row-gap:26px}
.area{display:flex;flex-direction:column;align-items:center;gap:8px;font-size:10px;color:var(--muted)}

/* form */
.request{height:340px;padding-top:60px}
.request .wrap{display:flex;padding-left:80px;gap:60px}
.request h2{width:260px;margin-bottom:12px}
.request .lead{width:260px;font-size:11px;color:var(--muted)}
.form{display:grid;grid-template-columns:1fr 1fr;column-gap:28px;row-gap:16px;width:520px;padding-top:10px}
.field label{display:block;font-size:10px;color:var(--muted);margin-bottom:4px}
.field span{display:block;height:30px;background:var(--grey)}
.submit{grid-column:1;justify-self:start;background:var(--purple);color:var(--white);font-size:11px;padding:8px 22px}

/* ramavtal */
.frameworks{height:320px;padding-top:56px}
.frameworks .wrap{padding-left:80px}
.frameworks h2{margin-bottom:36px}
.partner-grid{display:grid;grid-template-columns:repeat(6,1fr);gap:26px 30px}
.partner{height:34px;background:#d8d8dc}

/* quote */
.quote{height:180px;padding-top:50px}
.quote .wrap{display:flex;gap:24px;padding-left:140px}
.quote blockquote{width:560px;font-size:13px;font-weight:600}
.quote cite{display:block;margin-top:10px;font-size:10px;font-style:normal;color:var(--muted);font-weight:400}

/* uppdrag */
.jobs{height:300px;padding-top:40px}
.jobs .wrap{display:flex;gap:70px}
.jobs-left{width:300px}
.jobs-left h2{margin-bottom:20px}
.jobs-photo{height:150px;position:relative}
.jobs-photo .btn{position:absolute;left:20px;bottom:16px;background:var(--purple);color:var(--white);font-size:10px;padding:7px 14px}
.job-list{width:520px;list-style:none;padding-top:20px}
.job-list li{display:flex;justify-content:space-between;align-items:center;border-bottom:1px solid var(--line);padding:12px 0}
.job-list b{display:block;font-size:12px}
.job-list small{font-size:10px;color:var(--muted)}

/* om */
.about{height:500px;padding-top:50px}
.about .wrap{padding-left:80px}
.about h2{margin-bottom:16px}
.about p{width:520px;font-size:11px;color:var(--muted);margin-bottom:20px}
.about-photos{display:flex;gap:10px;margin-bottom:22px}
.about-photos div{height:150px}

/* msp */
.msp{height:270px;padding-top:50px}
.msp .wrap{display:flex;gap:60px;padding-left:80px}
.msp-text{width:360px}
.msp-text h2{margin-bottom:16px}
.msp-text p{font-size:11px;color:var(--muted)}
.msp-list{display:grid;grid-template-columns:1fr 1fr;gap:18px 40px;padding-top:50px;list-style:none}
.msp-list li{display:flex;align-items:center;gap:10px;font-size:11px}

/* team */
.team{height:310px;padding-top:44px}
.team .wrap{padding-left:80px}
.team h2{margin-bottom:28px}
.team-grid{display:flex;gap:50px}
.member{width:170px;height:180px;background:var(--grey);display:flex;flex-direction:column;align-items:center;padding-top:24px}
.avatar{width:70px;height:70px;border-radius:50%;background:linear-gradient(135deg,var(--photo-a),var(--photo-b));margin-bottom:14px}
.member b{font-size:12px}
.member small{font-size:10px;color:var(--muted)}

/* nyheter */
.news{height:300px;padding-top:50px}
.news .wrap{display:flex;gap:60px;padding-left:80px}
.news h2{width:260px}
.news-list{list-style:none;width:520px}
.news-list li{border-bottom:1px solid var(--line);padding:14px 0;font-size:11px}
.news-list small{display:block;color:var(--muted);font-size:10px}

/* footer */
.site-footer{height:90px;border-top:1px solid var(--line)}
.site-footer .wrap{display:flex;justify-content:space-between;align-items:center;height:90px;font-size:10px;color:var(--muted)}
.site-footer span{display:flex;align-items:center;gap:6px}
</style>
</head>
<body>

<header class="site-header">
  <div class="wrap">
    <div class="brand"><span class="brand-dot"></span>Tarnova</div>
    <nav class="nav"><span>Hem</span><span>Konsultuppdrag</span><span>Om oss</span><span class="cta">Kontakt</span></nav>
  </div>
</header>

<section class="section hero">
  <div class="wrap">
    <div>
      <p class="kicker">Konsultmäklare i Sverige</p>
      <h1>Vi Förenklar Ert Inköp av Kompetens</h1>
    </div>
    <p class="hero-aside">Rätt konsult<br>till rätt uppdrag<br>varje gång.</p>
  </div>
</section>
<div class="hero-photo photo" role="img" aria-label="Foto: tre kollegor i ett möte vid ett bord"></div>

<section class="section seek">
  <div class="wrap">
    <span class="side-label">Uppdrag</span>
    <h2>Söker Du Spetskompetens?</h2>
    <p>Vi hjälper konsulter och konsultbolag att hitta uppdrag som matchar deras kompetens. Registrera din profil så kontaktar vi dig när ett passande uppdrag dyker upp hos någon av våra kunder.</p>
    <ul class="ticks">
      <li><svg width="14" height="14" viewBox="0 0 14 14"><circle cx="7" cy="7" r="6" fill="none" stroke="#5a2d91"/><path d="M4 7l2 2 4-4" fill="none" stroke="#5a2d91" stroke-width="1.5"/></svg>Få tillgång till uppdrag hos ledande företag inom offentlig och privat sektor.</li>
      <li><svg width="14" height="14" viewBox="0 0 14 14"><circle cx="7" cy="7" r="6" fill="none" stroke="#5a2d91"/><path d="M4 7l2 2 4-4" fill="none" stroke="#5a2d91" stroke-width="1.5"/></svg>Personlig kontakt genom hela processen, från ansökan till avslut.</li>
      <li><svg width="14" height="14" viewBox="0 0 14 14"><circle cx="7" cy="7" r="6" fill="none" stroke="#5a2d91"/><path d="M4 7l2 2 4-4" fill="none" stroke="#5a2d91" stroke-width="1.5"/></svg>Snabb och trygg fakturering med betalning enligt avtal.</li>
    </ul>
  </div>
</section>

<section class="section grey areas">
  <div class="wrap">
    <span class="side-label">Kompetens</span>
    <span class="areas-badge">Tarnova</span>
    <h2>Ett Axplock Av Våra Kompetensområden</h2>
    <div class="area-grid">
      <div class="area"><svg width="32" height="32" viewBox="0 0 32 32" fill="none" stroke="#1d1d1f" stroke-width="1.5"><rect x="4" y="6" width="24" height="16" rx="2"/><path d="M10 27h12M16 22v5"/></svg>IT &amp; System</div>
      <div class="area"><svg width="32" height="32" viewBox="0 0 32 32" fill="none" stroke="#1d1d1f" stroke-width="1.5"><circle cx="16" cy="16" r="10"/><path d="M16 10v6l4 3"/></svg>Projektledning</div>
      <div class="area"><svg width="32" height="32" viewBox="0 0 32 32" fill="none" stroke="#1d1d1f" stroke-width="1.5"><path d="M6 26V14M13 26V8M20 26V16M27 26V10"/></svg>Ekonomi</div>
      <div class="area"><svg width="32" height="32" viewBox="0 0 32 32" fill="none" stroke="#1d1d1f" stroke-width="1.5"><circle cx="16" cy="11" r="5"/><path d="M6 27c1-6 5-9 10-9s9 3 10 9"/></svg>HR</div>
      <div class="area"><svg width="32" height="32" viewBox="0 0 32 32" fill="none" stroke="#1d1d1f" stroke-width="1.5"><rect x="6" y="5" width="20" height="23" rx="2"/><path d="M11 12h10M11 17h10M11 22h6"/></svg>Juridik</div>
      <div class="area"><svg width="32" height="32" viewBox="0 0 32 32" fill="none" stroke="#1d1d1f" stroke-width="1.5"><path d="M5 26l8-9 5 5 9-12"/></svg>Analys</div>
      <div class="area"><svg width="32" height="32" viewBox="0 0 32 32" fill="none" stroke="#1d1d1f" stroke-width="1.5"><rect x="5" y="10" width="22" height="16" rx="2"/><path d="M12 10V6h8v4"/></svg>Inköp</div>
      <div class="area"><svg width="32" height="32" viewBox="0 0 32 32" fill="none" stroke="#1d1d1f" stroke-width="1.5"><path d="M16 4l10 5v7c0 6-4 10-10 12-6-2-10-6-10-12V9z"/></svg>Säkerhet</div>
      <div class="area"><svg width="32" height="32" viewBox="0 0 32 32" fill="none" stroke="#1d1d1f" stroke-width="1.5"><circle cx="16" cy="16" r="4"/><path d="M16 4v5M16 23v5M4 16h5M23 16h5"/></svg>Teknik</div>
      <div class="area"><svg width="32" height="32" viewBox="0 0 32 32" fill="none" stroke="#1d1d1f" stroke-width="1.5"><path d="M5 8h22v14H13l-6 5v-5H5z"/></svg>Kommunikation</div>
      <div class="area"><svg width="32" height="32" viewBox="0 0 32 32" fill="none" stroke="#1d1d1f" stroke-width="1.5"><path d="M6 26h20M9 26V12M16 26V12M23 26V12M5 12l11-7 11 7"/></svg>Offentlig sektor</div>
      <div class="area"><svg width="32" height="32" viewBox="0 0 32 32" fill="none" stroke="#1d1d1f" stroke-width="1.5"><rect x="5" y="5" width="9" height="9"/><rect x="18" y="5" width="9" height="9"/><rect x="5" y="18" width="9" height="9"/><rect x="18" y="18" width="9" height="9"/></svg>Verksamhet</div>
      <div class="area"><svg width="32" height="32" viewBox="0 0 32 32" fill="none" stroke="#1d1d1f" stroke-width="1.5"><path d="M10 8l-6 8 6 8M22 8l6 8-6 8"/></svg>Utveckling</div>
      <div class="area"><svg width="32" height="32" viewBox="0 0 32 32" fill="none" stroke="#1d1d1f" stroke-width="1.5"><ellipse cx="16" cy="8" rx="10" ry="4"/><path d="M6 8v16c0 2 4 4 10 4s10-2 10-4V8"/></svg>Data</div>
      <div class="area"><svg width="32" height="32" viewBox="0 0 32 32" fill="none" stroke="#1d1d1f" stroke-width="1.5"><path d="M6 24c4 0 6-16 10-16s6 16 10 16"/></svg>Marknad</div>
      <div class="area"><svg width="32" height="32" viewBox="0 0 32 32" fill="none" stroke="#1d1d1f" stroke-width="1.5"><path d="M10 14l6-8 6 8M16 6v20M8 26h16"/></svg>Strategi</div>
      <div class="area"><svg width="32" height="32" viewBox="0 0 32 32" fill="none" stroke="#1d1d1f" stroke-width="1.5"><circle cx="16" cy="16" r="10"/><path d="M11 16l3 3 7-7"/></svg>Kvalitet</div>
      <div class="area"><svg width="32" height="32" viewBox="0 0 32 32" fill="none" stroke="#1d1d1f" stroke-width="1.5"><path d="M4 16h24M16 4c5 4 5 20 0 24M16 4c-5 4-5 20 0 24"/><circle cx="16" cy="16" r="12"/></svg>Miljö</div>
    </div>
  </div>
</section>

<section class="section request">
  <div class="wrap">
    <span class="side-label">Kontakt</span>
    <div>
      <h2>Söker Ni Kompetens?</h2>
      <p class="lead">Berätta vad ni behöver så återkommer vi med lämpliga kandidater inom kort.</p>
    </div>
    <div class="form">
      <div class="field"><label>Namn</label><span></span></div>
      <div class="field"><label>Företag</label><span></span></div>
      <div class="field"><label>E-post</label><span></span></div>
      <div class="field"><label>Telefon</label><span></span></div>
      <div class="field"><label>Roll</label><span></span></div>
      <div class="field"><label>Önskad startdatum</label><span></span></div>
      <span class="submit">Skicka</span>
    </div>
  </div>
</section>

<section class="section grey frameworks">
  <div class="wrap">
    <span class="side-label">Ramavtal</span>
    <h2>Urval Av<br>Våra Ramavtal</h2>
    <div class="partner-grid">
      <div class="partner"></div><div class="partner"></div><div class="partner"></div><div class="partner"></div><div class="partner"></div><div class="partner"></div>
      <div class="partner"></div><div class="partner"></div><div class="partner"></div><div class="partner"></div><div class="partner"></div><div class="partner"></div>
    </div>
  </div>
</section>

<section class="section quote">
  <div class="wrap">
    <svg width="26" height="22" viewBox="0 0 26 22"><path d="M0 22V12C0 5 4 1 10 0v4c-3 1-5 4-5 7h5v11zM16 22V12c0-7 4-11 10-12v4c-3 1-5 4-5 7h5v11z" fill="#5a2d91"/></svg>
    <blockquote>Tarnova hittade rätt konsult på rekordtid. Samarbetet har varit smidigt från första samtal till avslutat uppdrag och vi anlitar dem gärna igen.
      <cite>Inköpschef, Nordby Kommun</cite></blockquote>
  </div>
</section>

<section class="section grey jobs">
  <div class="wrap">
    <div class="jobs-left">
      <h2>Aktuella Uppdrag</h2>
      <div class="jobs-photo photo" role="img" aria-label="Foto: konsult som arbetar vid en dator"><span class="btn">Se alla uppdrag</span></div>
    </div>
    <ul class="job-list">
      <li><div><b>Systemutvecklare</b><small>Stockholm · Start omgående</small></div><svg width="10" height="10" viewBox="0 0 10 10"><path d="M2 3l3 3 3-3" fill="none" stroke="#1d1d1f"/></svg></li>
      <li><div><b>Projektledare IT</b><small>Göteborg · 12 månader</small></div><svg width="10" height="10" viewBox="0 0 10 10"><path d="M2 3l3 3 3-3" fill="none" stroke="#1d1d1f"/></svg></li>
      <li><div><b>Senior verksamhetsanalytiker</b><small>Malmö · Distans möjligt</small></div><svg width="10" height="10" viewBox="0 0 10 10"><path d="M2 3l3 3 3-3" fill="none" stroke="#1d1d1f"/></svg></li>
      <li><div><b>Informationssäkerhet</b><small>Uppsala · 6 månader</small></div><svg width="10" height="10" viewBox="0 0 10 10"><path d="M2 3l3 3 3-3" fill="none" stroke="#1d1d1f"/></svg></li>
    </ul>
  </div>
</section>

<section class="section about">
  <div class="wrap">
    <span class="side-label">Om oss</span>
    <h2>Om<br>Tarnova</h2>
    <p>Tarnova är en svensk konsultmäklare som kopplar samman kunder med erfarna konsulter. Vi arbetar nära både beställare och konsulter för att skapa långsiktiga samarbeten.</p>
    <div class="about-photos">
      <div class="photo" style="width:300px" role="img" aria-label="Foto: kollegor som samtalar"></div>
      <div class="photo" style="width:260px" role="img" aria-label="Foto: team vid en bärbar dator"></div>
      <div class="photo" style="width:280px" role="img" aria-label="Foto: möte i ett ljust kontor"></div>
    </div>
    <p>Med ett brett nätverk och många ramavtal kan vi snabbt leverera rätt kompetens. Vår ambition är att göra inköp av konsulttjänster enkelt, tryggt och effektivt för alla parter.</p>
  </div>
</section>

<section class="section grey msp">
  <div class="wrap">
    <div class="msp-text">
      <h2>MSP</h2>
      <p>Som Managed Service Provider tar vi helhetsansvar för er konsultförsörjning. Vi hanterar avrop, avtal, uppföljning och fakturering så att ni kan fokusera på er kärnverksamhet.</p>
    </div>
    <ul class="msp-list">
      <li><svg width="22" height="16" viewBox="0 0 22 16"><rect x="1" y="1" width="20" height="14" rx="3" fill="none" stroke="#5a2d91" stroke-width="1.5"/></svg>Avropshantering</li>
      <li><svg width="22" height="16" viewBox="0 0 22 16"><rect x="1" y="1" width="20" height="14" rx="3" fill="none" stroke="#5a2d91" stroke-width="1.5"/></svg>Leverantörsstyrning</li>
      <li><svg width="22" height="16" viewBox="0 0 22 16"><rect x="1" y="1" width="20" height="14" rx="3" fill="none" stroke="#5a2d91" stroke-width="1.5"/></svg>Uppföljning</li>
      <li><svg width="22" height="16" viewBox="0 0 22 16"><rect x="1" y="1" width="20" height="14" rx="3" fill="none" stroke="#5a2d91" stroke-width="1.5"/></svg>Rapportering</li>
      <li><svg width="22" height="16" viewBox="0 0 22 16"><rect x="1" y="1" width="20" height="14" rx="3" fill="none" stroke="#5a2d91" stroke-width="1.5"/></svg>Fakturering</li>
      <li><svg width="22" height="16" viewBox="0 0 22 16"><rect x="1" y="1" width="20" height="14" rx="3" fill="none" stroke="#5a2d91" stroke-width="1.5"/></svg>Avtalsstöd</li>
    </ul>
  </div>
</section>

<section class="section team">
  <div class="wrap">
    <h2>Vi På<br>Tarnova</h2>
    <div class="team-grid">
      <div class="member"><div class="avatar" role="img" aria-label="Porträtt av medarbetare"></div><b>Elin Sandberg</b><small>VD</small></div>
      <div class="member"><div class="avatar" role="img" aria-label="Porträtt av medarbetare"></div><b>Jonas Berglind</b><small>Konsultansvarig</small></div>
      <div class="member"><div class="avatar" role="img" aria-label="Porträtt av medarbetare"></div><b>Sara Lindqvist</b><small>Kundansvarig</small></div>
    </div>
  </div>
</section>

<section class="section grey news">
  <div class="wrap">
    <h2>Nyheter</h2>
    <ul class="news-list">
      <li>Nytt ramavtal tecknat med region<small>12 mars</small></li>
      <li>Vi välkomnar en ny medarbetare till teamet<small>28 februari</small></li>
      <li>Så lyckas du med ditt nästa uppdrag<small>9 februari</small></li>
    </ul>
  </div>
</section>

<footer class="site-footer">
  <div class="wrap">
    <span>© Tarnova AB</span>
    <span><svg width="12" height="12" viewBox="0 0 12 12"><path d="M6 11s4-4 4-7a4 4 0 00-8 0c0 3 4 7 4 7z" fill="none" stroke="#6e6e73"/></svg>Storgatan 14, Stockholm</span>
    <span><svg width="12" height="12" viewBox="0 0 12 12"><path d="M2 1h3l1 3-2 1a7 7 0 003 3l1-2 3 1v3c-6 0-9-3-9-9z" fill="none" stroke="#6e6e73"/></svg>08-000 00 00</span>
    <span>info@tarnova.se</span>
  </div>
</footer>

</body>
</html>
```